Tolvir Laundry and Dry Cleaning Poster

We need a Poster and Window Sticker for our Laundry and Dry cleaning shop (TOLVIR LAUNDRY AND DRY CLEANING).
info we like on the design. Logo is included
Company Name: Tolvir Laundry and Dry Cleaning
Slogan: It Comes Back Clean
Location: Kwelmo-Danfi, Accra
Working Hours: Mon-Sat 8am to 5pm
Tel: +233 30 418 7262
email:info@tolvirwash.example
website: www.tolvirwash.example
fb: fb.com/tolvirwash

Target Market(s)

Laundry Shop

Colors
33a6d7
9bcb3b

```html
<!DOCTYPE html>
<html lang="en">
<head>
<meta charset="utf-8">
<title>Tolvir Laundry and Dry Cleaning Poster</title>
<link rel="stylesheet" href="https://fonts.googleapis.com/css2?family=Open+Sans:ital,wdth,wght@0,75..100,400..800;1,75..100,400..800&display=swap">
<style>
  :root {
    --brand-blue: #2089cf;
    --brand-green: #8cc63f;
    --logo-teal: #21b3a6;
    --photo-dark: #2b2826;
    --photo-mid: #4a4745;
    --white: #ffffff;
  }
  * { margin: 0; padding: 0; box-sizing: border-box; }
  html, body { width: 1019px; height: 1200px; overflow: hidden; background: var(--white); }
  body { font-family: "Open Sans", Arial, sans-serif; }
  .poster { position: relative; width: 1019px; height: 1200px; overflow: hidden; background: var(--white); }
  .backdrop { position: absolute; inset: 0; }

  .brand { position: absolute; left: 32px; top: 112px; display: flex; align-items: center; gap: 14px; color: var(--brand-blue); font-weight: 600; }
  .brand-dot { width: 122px; height: 122px; border-radius: 50%; background: var(--logo-teal); }
  .brand-name { font-size: 86px; line-height: 0.9; letter-spacing: -1px; }
  .brand-tag { font-size: 14.5px; letter-spacing: 0.2px; margin-top: 8px; }

  .hours { position: absolute; right: 27px; top: 556px; text-align: right; color: var(--white); font-weight: 700; }
  .hours-title { font-size: 37px; letter-spacing: 3.5px; line-height: 1.2; margin-right: -2px; }
  .hours-days, .hours-time { font-size: 29px; letter-spacing: 2.4px; line-height: 1.25; }
  .hours-days { margin-top: 6px; }

  .contacts { position: absolute; left: 30px; top: 762px; list-style: none; }
  .contact { display: flex; align-items: center; height: 78px; color: var(--brand-blue); font-size: 35px; letter-spacing: 3.2px; }
  .contact svg { width: 58px; flex: none; margin-right: 24px; }
  .contact-address { height: 80px; }

  .slogan-band { position: absolute; left: 0; right: 0; bottom: 0; height: 70px; background: var(--brand-blue); display: flex; align-items: center; justify-content: center; }
  .slogan { color: var(--white); font-style: italic; font-weight: 700; font-stretch: 75%; font-size: 45px; letter-spacing: 2.4px; }
</style>
</head>
<body>
<main class="poster">
  <svg class="backdrop" width="1019" height="1200" viewBox="0 0 1019 1200">
    <defs>
      <linearGradient id="machineTone" x1="0" y1="0" x2="1" y2="1">
        <stop offset="0" stop-color="var(--photo-mid)"/>
        <stop offset="0.5" stop-color="#3a3735"/>
        <stop offset="1" stop-color="var(--photo-dark)"/>
      </linearGradient>
    </defs>
    <polygon points="300,0 1019,0 1019,930 46,510 538,168" fill="url(#machineTone)" role="img" aria-label="Photo of a front-loading washing machine with its door open"/>
    <polyline points="292,0 544,168 48,514" fill="none" stroke="var(--brand-green)" stroke-width="9"/>
    <line x1="0" y1="492" x2="1019" y2="936" stroke="var(--brand-blue)" stroke-width="11"/>
  </svg>

  <header class="brand">
    <span class="brand-dot"></span>
    <div>
      <div class="brand-name">Tolvir</div>
      <div class="brand-tag">LAUNDRY AND DRY CLEANING</div>
    </div>
  </header>

  <section class="hours">
    <h2 class="hours-title">WORKING HOURS</h2>
    <p class="hours-days">Monday-Saturday</p>
    <p class="hours-time">8am to 5pm</p>
  </section>

  <ul class="contacts">
    <li class="contact contact-address">
      <svg viewBox="0 0 58 72" height="72"><path d="M29 2C14 2 4 13 4 27c0 17 25 43 25 43s25-26 25-43C54 13 44 2 29 2z" fill="var(--brand-blue)"/><circle cx="29" cy="26" r="10" fill="var(--white)"/></svg>
      <span>Kwelmo-Danfi, Accra</span>
    </li>
    <li class="contact">
      <svg viewBox="0 0 58 54" height="54"><rect x="6" y="2" width="46" height="50" rx="6" fill="var(--brand-blue)"/><path d="M22 13c-4 2-5 6-3 13s6 13 10 15c3 1 5 0 7-2l-4-6-3 1c-2-2-4-6-4-9l3-2-2-8z" fill="var(--white)"/></svg>
      <span>+233 30 418 7262</span>
    </li>
    <li class="contact">
      <svg viewBox="0 0 58 46" height="46"><rect x="4" y="3" width="50" height="40" fill="var(--brand-blue)"/><path d="M6 6l23 20L52 6M6 40l17-16M52 40L35 24" fill="none" stroke="var(--white)" stroke-width="2.5"/></svg>
      <span>info@tolvirwash.example</span>
    </li>
    <li class="contact">
      <svg viewBox="0 0 58 58" height="58"><g fill="none" stroke="var(--brand-blue)" stroke-width="2.5"><circle cx="29" cy="29" r="26"/><ellipse cx="29" cy="29" rx="12" ry="26"/><line x1="29" y1="3" x2="29" y2="55"/><line x1="3" y1="29" x2="55" y2="29"/><path d="M7 16h44M7 42h44"/></g></svg>
      <span>www.tolvirwash.example</span>
    </li>
  </ul>

  <footer class="slogan-band">
    <p class="slogan">It Comes Back Clean</p>
  </footer>
</main>
</body>
</html>
```